Equipment Finance Specialist I work with companies who need the funds to buy their equipment

I would like a business card that stands out on the shelves. I want to be able to hand it to someone and say WOW. This card should have my logo.
You can put color into it I am very open on design and color

What my company does is we deal with dealerships that sell equipment such as Dump Trucks garbage trucks tractors trailers. Customers get referred to us and depending on their time in business we will ask for the following items

Companies that have been in business for more than two years we have a credit application program up to 250K . With this program we need the following items Credit application filled out(which is what I would like to be able for the customer to click on my website to get.) as well as three current month bank statements.

Deals over 250k we will need the following items

2 years business tax returns
2 years personal tax returns
Profit & Loss statement
Personal Financial Statement

what we do
100% FINANCING
SEASONAL PAYMENTS
LOAN BALLOON PAYMENTS
TRAC LEASING
LOW-INTEREST REFINANCING RATES
DEBT CONSOLIDATION

We specialize in creative financing solutions and offer a variety of reliable, flexible and expandable lending choices.

Target Market(s)

Trucking Companies

Industry/Entity Type

Trucking Company

Contact Information for Business Card

* $250,000 Application only Program
* Loans from $30,000 to 5,000,000
* Competitive Interest Rates

Font styles to use
Serif
Sans Serif

Colors

Designer to choose colors to be used in the design.

Requirements
Must have
• On the back of the card.
• * $250,000 Application only Program
• * Loans from $30,000 to 5,000,000
• My name, email, website. address
• * Competitive Interest Rates
• * 100% Financing
Nice to have
• I want my logo to pop on the card
• My logo is the great one I would like to use
Should not have
• I am up for your creativity as well

```html
<!DOCTYPE html>
<html lang="en">
<head>
<meta charset="utf-8">
<title>Ridgeway Funding — Business Card</title>
<link rel="stylesheet" href="https://fonts.googleapis.com/css2?family=Libre+Baskerville:wght@700&family=Montserrat:wght@400;500;700&display=swap">
<style>
  :root {
    --backdrop: #1e1e1f;
    --paper: #ffffff;
    --navy: #1f2d6e;
    --red: #e1262c;
    --ink: #1b1b1b;
    --mist: #eceef2;
    --charcoal: #2a2728;
    --charcoal-deep: #171516;
    --silver: #d9d9dc;
  }
  * { box-sizing: border-box; margin: 0; padding: 0; }
  html, body {
    width: 1200px; height: 900px; overflow: hidden;
    background: var(--backdrop);
    font-family: "Montserrat", Arial, sans-serif;
  }
  .stage {
    width: 1200px; height: 900px;
    display: flex; flex-direction: column; align-items: center; justify-content: center;
    gap: 56px;
  }
  .card {
    position: relative;
    width: 600px; height: 343px;
    border-radius: 4px;
    overflow: hidden;
    box-shadow: 0 14px 30px rgba(0,0,0,.55);
  }

  /* Front */
  .card-front { background: var(--paper); color: var(--ink); }
  .truck-decoration {
    position: absolute; right: 40px; top: 0;
    width: 220px; height: 150px;
    background: radial-gradient(ellipse at center, var(--mist) 0%, rgba(236,238,242,0) 70%);
  }
  .brand {
    position: absolute; left: 40px; top: 52px;
    display: flex; align-items: center; gap: 12px;
  }
  .brand-dot {
    width: 50px; height: 50px; border-radius: 50%;
    background: var(--navy); flex: none;
  }
  .brand-name {
    font-weight: 700; font-size: 25px; line-height: 1.05;
    color: var(--navy); letter-spacing: .5px; text-transform: uppercase;
  }
  .card-front .brand-name { display: block; width: 150px; }
  .holder {
    position: absolute; right: 60px; top: 70px; text-align: left;
    white-space: nowrap;
  }
  .holder-name {
    font-family: "Libre Baskerville", "Times New Roman", serif;
    font-weight: 700; font-size: 22px; letter-spacing: -.5px; color: var(--ink);
  }
  .holder-position {
    font-size: 14px; letter-spacing: 4px; color: var(--navy); margin-top: 4px; margin-left: 46px;
  }
  .contact-band {
    position: absolute; left: 0; right: 0; top: 160px; height: 78px;
    background: var(--navy);
    border-bottom: 5px solid var(--red);
    display: flex; justify-content: space-between; align-items: center;
    padding: 0 38px 0 44px;
    color: var(--paper);
  }
  .contact-list { list-style: none; display: flex; flex-direction: column; gap: 6px; }
  .contact-list li { display: flex; align-items: center; gap: 10px; font-size: 17px; white-space: nowrap; }
  .contact-list svg { width: 14px; height: 14px; flex: none; }
  .offers {
    position: absolute; left: 44px; right: 30px; top: 262px;
    display: flex; gap: 28px;
    font-size: 14px; color: var(--ink);
  }
  .offers ul { list-style: none; display: flex; flex-direction: column; gap: 5px; }
  .offers li { white-space: nowrap; }
  .offers li::before { content: "•"; margin-right: 8px; }

  /* Back */
  .card-back { background: var(--charcoal-deep); }
  .fabric-texture {
    position: absolute; inset: 0;
    background: radial-gradient(ellipse at 45% 45%, var(--charcoal) 0%, var(--charcoal-deep) 85%);
  }
  .back-brand {
    position: absolute; inset: 0;
    display: flex; align-items: center; justify-content: center; gap: 18px;
  }
  .back-brand .brand-dot {
    width: 70px; height: 70px; background: var(--silver);
  }
  .back-brand .brand-name { color: var(--silver); font-size: 36px; white-space: nowrap; }
</style>
</head>
<body>
<main class="stage">

  <section class="card card-front" aria-label="Card front">
    <div class="truck-decoration" role="img" aria-label="Faint illustration of a work truck"></div>

    <div class="brand">
      <span class="brand-dot"></span>
      <span class="brand-name">Ridgeway Funding</span>
    </div>

    <div class="holder">
      <p class="holder-name">YOUR NAME</p>
      <p class="holder-position">Position</p>
    </div>

    <div class="contact-band">
      <ul class="contact-list">
        <li>
          <svg viewBox="0 0 24 24" fill="currentColor" aria-hidden="true"><path d="M6.6 10.8a15.1 15.1 0 0 0 6.6 6.6l2.2-2.2a1 1 0 0 1 1-.25 11.4 11.4 0 0 0 3.6.57 1 1 0 0 1 1 1V20a1 1 0 0 1-1 1A17 17 0 0 1 3 4a1 1 0 0 1 1-1h3.5a1 1 0 0 1 1 1c0 1.250.2 2.450.57 3.570a1 1 0 0 1-.25 1z"/></svg>
          phone number
        </li>
        <li>
          <svg viewBox="0 0 24 24" fill="none" stroke="currentColor" stroke-width="2" aria-hidden="true"><rect x="2" y="5" width="20" height="14"/><path d="M2 5l10 8 10-8"/></svg>
          info@ridgewayfunding.com
        </li>
      </ul>
      <ul class="contact-list">
        <li>
          <svg viewBox="0 0 24 24" fill="none" stroke="currentColor" stroke-width="2" aria-hidden="true"><circle cx="12" cy="12" r="10"/><path d="M2 12h20M12 2c3 3 3 17 0 20M12 2c-3 3-3 17 0 20"/></svg>
          ridgewayfunding.com
        </li>
        <li>
          <svg viewBox="0 0 24 24" fill="currentColor" aria-hidden="true"><path d="M12 2a7 7 0 0 0-7 7c0 5 7 13 7 13s7-8 7-13a7 7 0 0 0-7-7zm0 9.5A2.5 2.5 0 1 1 12 6.5a2.5 2.5 0 0 1 0 5z"/></svg>
          office address
        </li>
      </ul>
    </div>

    <div class="offers">
      <ul>
        <li>$250,000 Application only Program</li>
        <li>Loans from $30,000 to 5,000,000</li>
      </ul>
      <ul>
        <li>Competitive Interest Rates</li>
        <li>100% Financing</li>
      </ul>
    </div>
  </section>

  <section class="card card-back" aria-label="Card back">
    <div class="fabric-texture" role="img" aria-label="Dark woven fabric texture"></div>
    <div class="back-brand">
      <span class="brand-dot"></span>
      <span class="brand-name">Ridgeway Funding</span>
    </div>
  </section>

</main>
</body>
</html>
```